Baby acupressure app for parents

We need an app for parents that teaches parents how to help them relieve their baby's imbalances (stomach ache, trouble sleeping etc.)

Please see the attached document (with info) and wireframes.

This project is urgent so please only participate if you're able to finish all screens within a few days after the contest is over.

Target Market(s)

Baby moms (20-40 years of age)

Industry/Entity Type

Baby Care

Colors
886aae
b768aa
e667a6
f68d4d
faa54b
fac994
f9ba93
f59195
fee18a

Requirements
Must have
• A high quality design that is both modern and very sleek and stylish.
Nice to have
• Simple animations to make the app "feel" like it's extreme high quality and make the user want to use it again and again
Should not have
• Sandwich menus

```html
<!DOCTYPE html>
<html lang="en">
<head>
<meta charset="utf-8">
<title>Nestly – Baby Acupressure App Screens</title>
<link rel="stylesheet" href="https://fonts.googleapis.com/css2?family=Inter:wght@400;500;600&family=Lato:wght@300;400;700&display=swap">
<style>
  :root {
    --violet: #886aae;
    --orchid: #b768aa;
    --rose: #e667a6;
    --orange: #f68d4d;
    --amber: #faa54b;
    --peach: #fac994;
    --apricot: #f9ba93;
    --salmon: #f59195;
    --lemon: #fee18a;
    --periwinkle: #7f8ff0;
    --lilac: #a47ce0;
    --paper: #f2f3f7;
    --ink: #1d1d22;
    --muted: #9a9aa6;
    --white: #ffffff;
  }
  * { box-sizing: border-box; margin: 0; padding: 0; }
  html, body { width: 1200px; height: 1200px; overflow: hidden; background: var(--white); }
  body { font-family: "Lato", sans-serif; color: var(--ink); }

  .stage { position: relative; width: 1500px; height: 1500px; transform: scale(0.8); transform-origin: 0 0; }

  .screen { position: absolute; width: 281px; height: 610px; overflow: hidden; box-shadow: 0 18px 40px rgba(60, 50, 90, 0.16); }
  .status { position: absolute; top: 10px; left: 21px; right: 14px; display: flex; justify-content: space-between; align-items: center; font-family: "Inter", sans-serif; font-size: 11px; }
  .status svg { display: block; }

  /* Onboarding */
  .onboard { color: var(--white); }
  .onboard .status { color: rgba(255,255,255,0.85); }
  .splash { background: linear-gradient(180deg, #7d8ef0 0%, #8f7ad9 50%, #a069c8 100%); }
  .splash-photo { position: absolute; inset: 0; background: radial-gradient(ellipse at 60% 35%, rgba(255,255,255,0.12), transparent 55%), radial-gradient(ellipse at 40% 80%, rgba(255,255,255,0.08), transparent 50%); }
  .brand { position: absolute; top: 330px; left: 0; right: 0; text-align: center; font-family: "Lato", sans-serif; font-weight: 300; font-size: 21px; letter-spacing: 1px; color: var(--white); }
  .brand-dot { display: block; width: 80px; height: 80px; margin: 0 auto 16px; border-radius: 50%; background: var(--white); }
  .slide-1 { background: linear-gradient(180deg, #f4a274 0%, #ee969a 45%, #d98aa4 70%, #9a7bcb 100%); }
  .slide-2 { background: linear-gradient(180deg, #f2a3a6 0%, #e98f9d 45%, #d98aa6 70%, #9b7bcb 100%); }
  .slide-3 { background: linear-gradient(180deg, #f1a3a9 0%, #e98fa0 45%, #d88ba8 70%, #9a7ccc 100%); }
  .hero-art { position: absolute; top: 120px; left: 0; right: 0; height: 175px; background: linear-gradient(180deg, rgba(255,255,255,0) 0%, rgba(250,201,148,0.45) 55%, rgba(230,103,166,0.25) 100%); }
  .hero-figure { position: absolute; top: 130px; left: 100px; width: 80px; height: 160px; border-radius: 40px; background: linear-gradient(180deg, var(--peach), var(--rose)); opacity: 0.85; }
  .slide-title { position: absolute; top: 326px; left: 0; right: 0; text-align: center; font-size: 15.5px; font-weight: 300; letter-spacing: 1.4px; line-height: 21px; color: rgba(255,255,255,0.92); }
  .pager { position: absolute; top: 410px; left: 0; right: 0; display: flex; justify-content: center; gap: 7px; }
  .pager span { width: 10px; height: 10px; border-radius: 50%; border: 1px solid rgba(255,255,255,0.9); }
  .pager .on { background: var(--white); }
  .pill { position: absolute; top: 471px; left: 59px; width: 162px; height: 40px; border-radius: 20px; background: linear-gradient(90deg, var(--periwinkle), var(--lilac)); color: var(--white); font-family: "Inter", sans-serif; font-size: 8px; font-weight: 600; letter-spacing: 0.5px; display: flex; align-items: center; justify-content: center; gap: 40px; box-shadow: 0 6px 14px rgba(90, 80, 180, 0.25); }
  .disclaimer { position: absolute; top: 561px; left: 10px; right: 10px; text-align: center; font-size: 8px; line-height: 14px; letter-spacing: 0.4px; color: rgba(255,255,255,0.8); }
  .disclaimer b { font-weight: 700; color: var(--white); }

  /* App screens */
  .app { background: var(--paper); }
  .app .status { color: var(--ink); }
  .back { position: absolute; top: 44px; left: 12px; }
  .page-title { position: absolute; top: 69px; left: 21px; font-family: "Inter", sans-serif; font-size: 26px; font-weight: 500; letter-spacing: -0.3px; display: flex; align-items: center; gap: 8px; }
  .page-title.with-icon { left: 13px; }
  .title-icon { width: 24px; height: 24px; border-radius: 50%; background: linear-gradient(135deg, var(--lilac), var(--rose)); }
  .deco-orange { position: absolute; top: 40px; left: 197px; width: 220px; height: 220px; border-radius: 50%; background: linear-gradient(160deg, var(--orange), var(--salmon)); }
  .deco-violet { position: absolute; top: 378px; left: -130px; width: 230px; height: 170px; border-radius: 0 0 120px 0; background: linear-gradient(180deg, var(--lilac), var(--periwinkle)); }

  .imbalance { position: absolute; left: 11px; width: 258px; height: 127px; display: flex; background: var(--white); box-shadow: 0 6px 16px rgba(60, 50, 90, 0.12); }
  .imbalance-icon { width: 74px; display: flex; align-items: center; justify-content: center; }
  .imbalance-icon span { width: 34px; height: 34px; border-radius: 50%; background: linear-gradient(135deg, var(--orchid), var(--amber)); }
  .imbalance-photo { position: relative; flex: 1; padding: 66px 14px 0; color: var(--white); }
  .imbalance-photo h3 { font-family: "Inter", sans-serif; font-size: 15.5px; font-weight: 400; }
  .imbalance-photo p { font-size: 8px; line-height: 13px; margin-top: 4px; color: rgba(255,255,255,0.65); }
  .photo-colic { background: linear-gradient(135deg, #f0b0c0, #d98ab8); }
  .photo-growing { background: linear-gradient(135deg, #b2a2e6, #9b86de); }
  .photo-eczema { background: linear-gradient(135deg, #f6a47a, #e98a72); }

  .tabbar { position: absolute; bottom: 0; left: 0; right: 0; height: 60px; background: var(--white); display: flex; justify-content: space-around; padding-top: 14px; }
  .tab { width: 56px; display: flex; flex-direction: column; align-items: center; gap: 4px; font-family: "Inter", sans-serif; font-size: 4.5px; letter-spacing: 0.3px; color: #b4b4bf; text-transform: uppercase; }
  .tab.active { color: var(--orange); }
  .tab-notch { position: absolute; top: -6px; left: 100px; width: 10px; height: 6px; border-radius: 5px 5px 0 0; background: var(--orange); transform: rotate(180deg); }

  .detail-card { position: absolute; top: 109px; left: 13px; width: 256px; height: 371px; background: var(--white); box-shadow: 0 6px 16px rgba(60, 50, 90, 0.08); }
  .video { position: relative; height: 138px; background: linear-gradient(120deg, #efe6e2 0%, #f3d2bf 45%, #dde7ee 100%); }
  .play { position: absolute; top: 48px; left: 103px; width: 50px; height: 50px; border-radius: 50%; background: rgba(60,60,60,0.55); display: flex; align-items: center; justify-content: center; }
  .copy { font-size: 7.5px; line-height: 13px; color: var(--muted); }
  .copy-top { padding: 8px 16px 0; }
  .thumbs { display: flex; gap: 13px; padding: 10px 14px 0; }
  .thumbs span { width: 66px; height: 66px; }
  .thumbs span:nth-child(1) { background: linear-gradient(135deg, #d9dfe8, #e8b9a5); }
  .thumbs span:nth-child(2) { background: linear-gradient(135deg, #f3c8a8, #d99a82); }
  .thumbs span:nth-child(3) { background: linear-gradient(135deg, #e9b9a0, #c98b72); }
  .copy-bottom { padding: 8px 10px 0; }
  .more { position: absolute; bottom: 0; left: 0; right: 0; height: 36px; border-top: 1px solid #ececf1; display: flex; align-items: center; justify-content: center; font-family: "Inter", sans-serif; font-size: 8px; color: var(--lilac); }
  .pill.start { top: 493px; left: 54px; }

  .intro { position: absolute; top: 106px; left: 0; right: 0; height: 38px; background: var(--white); padding: 8px 14px 0; font-size: 7.5px; line-height: 13px; color: var(--muted); }
  .spot { position: absolute; width: 118px; height: 118px; border-radius: 3px; display: flex; flex-direction: column; align-items: center; justify-content: flex-end; padding-bottom: 10px; gap: 10px; color: var(--white); font-family: "Inter", sans-serif; font-size: 13px; font-weight: 500; box-shadow: 0 6px 14px rgba(60, 50, 90, 0.14); }
  .spot i { width: 44px; height: 44px; border-radius: 50%; background: rgba(255,255,255,0.85); }
  .spot-hands { top: 153px; left: 17px; background: linear-gradient(135deg, #f6a983, #e88a8e); }
  .spot-feet { top: 153px; left: 148px; background: linear-gradient(135deg, #8f9af0, #9d7fd8); }
  .spot-face { top: 282px; left: 17px; background: linear-gradient(135deg, #eea2ad, #dc8aa2); }
  .spot-body { top: 282px; left: 148px; background: linear-gradient(135deg, #b6a0c9, #d9a39c); }
  .bonus { position: absolute; top: 425px; left: 16px; width: 251px; height: 100px; background: var(--white); border: 1px solid #ececf1; }
  .bonus-ribbon { position: absolute; top: -3px; left: -6px; width: 116px; height: 26px; background: linear-gradient(90deg, var(--violet), var(--lilac)); transform: rotate(-8deg); }
  .bonus-text { position: absolute; top: 44px; left: 20px; font-size: 10.5px; line-height: 18px; letter-spacing: 0.6px; color: var(--muted); }
  .bonus-text b { color: var(--ink); font-weight: 700; }
  .bonus-photo { position: absolute; top: 0; right: 0; width: 90px; height: 100px; background: linear-gradient(135deg, #e9eef3, #cfdbe6); clip-path: polygon(0 0, 100% 0, 100% 100%, 40% 100%); }
</style>
</head>
<body>
<main class="stage">

  <!-- Splash -->
  <section class="screen onboard splash" style="left:91px; top:71px;">
    <div class="splash-photo" role="img" aria-label="Soft-focus photo of a parent holding a baby"></div>
    <div class="status"><span>9:41</span>
      <svg width="30" height="8" viewBox="0 0 30 8"><path d="M4 7 L1 3.5 A4.5 4.5 0 0 1 7 3.5 Z" fill="#fff"/><rect x="15" y="1.5" width="11" height="5.5" rx="1" fill="#fff"/><rect x="26.5" y="3" width="1.5" height="2.5" fill="#fff"/></svg></div>
    <div class="brand"><span class="brand-dot"></span>Nestly</div>
  </section>

  <!-- Onboarding 1 -->
  <section class="screen onboard slide-1" style="left:442px; top:71px;">
    <div class="status"><span>9:41</span>
      <svg width="30" height="8" viewBox="0 0 30 8"><path d="M4 7 L1 3.5 A4.5 4.5 0 0 1 7 3.5 Z" fill="#fff"/><rect x="15" y="1.5" width="11" height="5.5" rx="1" fill="#fff"/><rect x="26.5" y="3" width="1.5" height="2.5" fill="#fff"/></svg></div>
    <div class="hero-art" role="img" aria-label="Illustration of a crying swaddled baby above soft clouds"></div>
    <div class="hero-figure"></div>
    <h2 class="slide-title">Find your Child’s<br>Imbalances</h2>
    <div class="pager"><span class="on"></span><span></span><span></span></div>
    <div class="pill">Skip</div>
    <p class="disclaimer">Always consult a physician if you suspect your child<br>is in need of health care. See <b>FAQ</b> for more info.</p>
  </section>

  <!-- Onboarding 2 -->
  <section class="screen onboard slide-2" style="left:782px; top:71px;">
    <div class="status"><span>9:41</span>
      <svg width="30" height="8" viewBox="0 0 30 8"><path d="M4 7 L1 3.5 A4.5 4.5 0 0 1 7 3.5 Z" fill="#fff"/><rect x="15" y="1.5" width="11" height="5.5" rx="1" fill="#fff"/><rect x="26.5" y="3" width="1.5" height="2.5" fill="#fff"/></svg></div>
    <div class="hero-art" role="img" aria-label="Illustration of a doctor holding a clipboard above soft clouds"></div>
    <div class="hero-figure" style="background:linear-gradient(180deg,#f6e1cf,#ffffff);"></div>
    <h2 class="slide-title">Get help from<br>Experts</h2>
    <div class="pager"><span></span><span class="on"></span><span></span></div>
    <div class="pill">Skip</div>
    <p class="disclaimer">Always consult a physician if you suspect your child<br>is in need of health care. See <b>FAQ</b> for more info.</p>
  </section>

  <!-- Onboarding 3 -->
  <section class="screen onboard slide-3" style="left:1127px; top:71px;">
    <div class="status"><span>9:41</span>
      <svg width="30" height="8" viewBox="0 0 30 8"><path d="M4 7 L1 3.5 A4.5 4.5 0 0 1 7 3.5 Z" fill="#fff"/><rect x="15" y="1.5" width="11" height="5.5" rx="1" fill="#fff"/><rect x="26.5" y="3" width="1.5" height="2.5" fill="#fff"/></svg></div>
    <div class="hero-art" role="img" aria-label="Illustration of a calm swaddled baby above soft clouds"></div>
    <div class="hero-figure"></div>
    <h2 class="slide-title">Help relieve your<br>child’s imbalances</h2>
    <div class="pager"><span></span><span></span><span class="on"></span></div>
    <div class="pill"><span>BEGIN</span>
      <svg width="16" height="10" viewBox="0 0 16 10"><path d="M1 5 H14 M10 1 L14 5 L10 9" stroke="#fff" stroke-width="1.4" fill="none"/></svg></div>
    <p class="disclaimer">Always consult a physician if you suspect your child<br>is in need of health care. See <b>FAQ</b> for more info.</p>
  </section>

  <!-- Imbalances list -->
  <section class="screen app" style="left:91px; top:782px;">
    <div class="deco-orange"></div>
    <div class="deco-violet"></div>
    <div class="status"><span>9:41</span>
      <svg width="42" height="8" viewBox="0 0 42 8"><rect x="0" y="5" width="2" height="3" fill="#1d1d22"/><rect x="3" y="3.5" width="2" height="4.5" fill="#1d1d22"/><rect x="6" y="2" width="2" height="6" fill="#1d1d22"/><rect x="9" y="0.5" width="2" height="7.5" fill="#1d1d22"/><path d="M19 7 L15.5 3.5 A5 5 0 0 1 22.5 3.5 Z" fill="#1d1d22"/><rect x="27" y="1.5" width="11" height="5.5" rx="1" fill="#1d1d22"/><rect x="38.5" y="3" width="1.5" height="2.5" fill="#1d1d22"/></svg></div>
    <h1 class="page-title">Imbalances</h1>

    <article class="imbalance" style="top:113px;">
      <div class="imbalance-icon"><span></span></div>
      <div class="imbalance-photo photo-colic" role="img" aria-label="Photo of a crying newborn baby">
        <h3>Colic</h3><p>Long and frequent crying is<br>hard to deal with</p></div>
    </article>
    <article class="imbalance" style="top:256px;">
      <div class="imbalance-icon"><span></span></div>
      <div class="imbalance-photo photo-growing" role="img" aria-label="Photo of a sleeping baby">
        <h3>Growing Pains</h3><p>Relieve pain that comes from<br>growth spurts</p></div>
    </article>
    <article class="imbalance" style="top:398px;">
      <div class="imbalance-icon"><span></span></div>
      <div class="imbalance-photo photo-eczema" role="img" aria-label="Photo of a newborn lying down">
        <h3>Eczema</h3><p>Inflammation of the skin can<br>itch and hurt</p></div>
    </article>

    <nav class="tabbar">
      <span class="tab-notch"></span>
      <div class="tab"><svg width="20" height="20" viewBox="0 0 20 20" fill="none" stroke="#b4b4bf"><path d="M3 9 L10 3 L17 9 V17 H3 Z M8 17 V12 H12 V17"/></svg>Home</div>
      <div class="tab active"><svg width="20" height="20" viewBox="0 0 20 20" fill="none" stroke="#f68d4d"><circle cx="10" cy="10" r="8"/><circle cx="10" cy="10" r="3"/></svg>Imbalances</div>
      <div class="tab"><svg width="20" height="20" viewBox="0 0 20 20" fill="none" stroke="#b4b4bf"><circle cx="15" cy="4" r="2.2"/><circle cx="4" cy="10" r="2.2"/><circle cx="15" cy="16" r="2.2"/><path d="M6 9 L13 5 M6 11 L13 15"/></svg>Share</div>
      <div class="tab"><svg width="20" height="20" viewBox="0 0 20 20" fill="none" stroke="#b4b4bf"><circle cx="10" cy="10" r="8"/><path d="M10 9 V14 M10 6 V7"/></svg>About us</div>
    </nav>
  </section>

  <!-- Ear Pain detail -->
  <section class="screen app" style="left:436px; top:782px;">
    <div class="status"><span>9:41</span>
      <svg width="42" height="8" viewBox="0 0 42 8"><rect x="0" y="5" width="2" height="3" fill="#1d1d22"/><rect x="3" y="3.5" width="2" height="4.5" fill="#1d1d22"/><rect x="6" y="2" width="2" height="6" fill="#1d1d22"/><rect x="9" y="0.5" width="2" height="7.5" fill="#1d1d22"/><path d="M19 7 L15.5 3.5 A5 5 0 0 1 22.5 3.5 Z" fill="#1d1d22"/><rect x="27" y="1.5" width="11" height="5.5" rx="1" fill="#1d1d22"/><rect x="38.5" y="3" width="1.5" height="2.5" fill="#1d1d22"/></svg></div>
    <svg class="back" width="16" height="12" viewBox="0 0 16 12"><path d="M15 6 H2 M6 1 L1 6 L6 11" stroke="#1d1d22" stroke-width="1.5" fill="none"/></svg>
    <h1 class="page-title with-icon"><span class="title-icon"></span>Ear Pain</h1>

    <article class="detail-card">
      <div class="video" role="img" aria-label="Video still of a doctor holding a baby">
        <div class="play"><svg width="16" height="18" viewBox="0 0 16 18"><path d="M3 2 L14 9 L3 16 Z" stroke="#fff" stroke-width="1.3" fill="none"/></svg></div>
      </div>
      <p class="copy copy-top">Gentle pressure on the right spots can ease ear pain and help your little one settle down again.</p>
      <div class="thumbs" role="img" aria-label="Three photos of babies having their ears checked"><span></span><span></span><span></span></div>
      <p class="copy copy-bottom">There are multiple ways to trigger some positive effects and you can try out multiple spots/treatments… Also, check out the bonus info from our expert who also offers some great advice on this topic!</p>
      <div class="more">More details</div>
    </article>
    <div class="pill start">START NOW</div>

    <nav class="tabbar">
      <span class="tab-notch"></span>
      <div class="tab"><svg width="20" height="20" viewBox="0 0 20 20" fill="none" stroke="#b4b4bf"><path d="M3 9 L10 3 L17 9 V17 H3 Z M8 17 V12 H12 V17"/></svg>Home</div>
      <div class="tab active"><svg width="20" height="20" viewBox="0 0 20 20" fill="none" stroke="#f68d4d"><circle cx="10" cy="10" r="8"/><circle cx="10" cy="10" r="3"/></svg>Imbalances</div>
      <div class="tab"><svg width="20" height="20" viewBox="0 0 20 20" fill="none" stroke="#b4b4bf"><circle cx="15" cy="4" r="2.2"/><circle cx="4" cy="10" r="2.2"/><circle cx="15" cy="16" r="2.2"/><path d="M6 9 L13 5 M6 11 L13 15"/></svg>Share</div>
      <div class="tab"><svg width="20" height="20" viewBox="0 0 20 20" fill="none" stroke="#b4b4bf"><circle cx="10" cy="10" r="8"/><path d="M10 9 V14 M10 6 V7"/></svg>About us</div>
    </nav>
  </section>

  <!-- Ear Pain spots -->
  <section class="screen app" style="left:782px; top:782px;">
    <div class="status"><span>9:41</span>
      <svg width="42" height="8" viewBox="0 0 42 8"><rect x="0" y="5" width="2" height="3" fill="#1d1d22"/><rect x="3" y="3.5" width="2" height="4.5" fill="#1d1d22"/><rect x="6" y="2" width="2" height="6" fill="#1d1d22"/><rect x="9" y="0.5" width="2" height="7.5" fill="#1d1d22"/><path d="M19 7 L15.5 3.5 A5 5 0 0 1 22.5 3.5 Z" fill="#1d1d22"/><rect x="27" y="1.5" width="11" height="5.5" rx="1" fill="#1d1d22"/><rect x="38.5" y="3" width="1.5" height="2.5" fill="#1d1d22"/></svg></div>
    <svg class="back" width="16" height="12" viewBox="0 0 16 12"><path d="M15 6 H2 M6 1 L1 6 L6 11" stroke="#1d1d22" stroke-width="1.5" fill="none"/></svg>
    <h1 class="page-title with-icon"><span class="title-icon"></span>Ear Pain</h1>
    <p class="intro">There are multiple was to help relieve your child's ear pain.<br>Select a spot to get started…</p>

    <div class="spot spot-hands" role="img" aria-label="Photo of a baby hand with hand icon"><i></i>HANDS</div>
    <div class="spot spot-feet" role="img" aria-label="Photo of baby feet with feet icon"><i></i>FEET</div>
    <div class="spot spot-face" role="img" aria-label="Photo of a baby with face icon"><i></i>FACE</div>
    <div class="spot spot-body" role="img" aria-label="Photo of a sitting baby with body icon"><i></i>BODY</div>

    <aside class="bonus">
      <div class="bonus-ribbon" role="img" aria-label="Hand-lettered bonus ribbon"></div>
      <p class="bonus-text">Get some additional<br>advice from <b>DR ALMA</b></p>
      <div class="bonus-photo" role="img" aria-label="Photo of a smiling doctor"></div>
    </aside>

    <nav class="tabbar">
      <span class="tab-notch"></span>
      <div class="tab"><svg width="20" height="20" viewBox="0 0 20 20" fill="none" stroke="#b4b4bf"><path d="M3 9 L10 3 L17 9 V17 H3 Z M8 17 V12 H12 V17"/></svg>Home</div>
      <div class="tab active"><svg width="20" height="20" viewBox="0 0 20 20" fill="none" stroke="#f68d4d"><circle cx="10" cy="10" r="8"/><circle cx="10" cy="10" r="3"/></svg>Imbalances</div>
      <div class="tab"><svg width="20" height="20" viewBox="0 0 20 20" fill="none" stroke="#b4b4bf"><circle cx="15" cy="4" r="2.2"/><circle cx="4" cy="10" r="2.2"/><circle cx="15" cy="16" r="2.2"/><path d="M6 9 L13 5 M6 11 L13 15"/></svg>Share</div>
      <div class="tab"><svg width="20" height="20" viewBox="0 0 20 20" fill="none" stroke="#b4b4bf"><circle cx="10" cy="10" r="8"/><path d="M10 9 V14 M10 6 V7"/></svg>About us</div>
    </nav>
  </section>

</main>
</body>
</html>
```